Fahrzeugbeschriftung für Hersteller von Campingzubehör
Perfekt! Genau das was wir uns vorgestellt haben. Vielen Dank
Zielgruppe
Wir sind Hersteller von Campingzubehör, made in Germany! Angesprochen werden sollen, Camper, Händler und Vermieter von Freizeitfahrzeugen. Hier soll ein Sonnensegel kreiert werden, als Werbemaßnahme für die o.g. Zielgruppe. Dieses Sonnensegel soll auf die Einzigartigkeit des Campers wieder spiegeln. Für den schönsten Schatten der Welt!
Campen ist IN! und Individualität wird groß geschrieben. Das Alter der Zielgruppe reicht von 42-80 und legt Wert auf Nachhaltigkeit, Qualität, schätzt den Komfort, aber eben auch das Hobby und die damit verbundene Reiselust.
Aufgabenstellung
Druckformat ist eines 3m breit und 2,2m hoch und 1m breit und 2,2m hoch, Druckvorlage ist dabei. Wichtig ist die HP
www.graylindtrailgear.com
Das Banner soll dann aussehen wie dies auf der erste Seite des Flyers

```html
<!DOCTYPE html>
<html lang="de">
<head>
<meta charset="utf-8">
<title>Sunblocker Banner – Graylind Trail Gear</title>
<link rel="stylesheet" href="https://fonts.googleapis.com/css2?family=Carlito:wght@400;700&display=swap">
<style>
  :root {
    --page: #ffffff;
    --leaf: #a0c550;
    --sun: #f3ea14;
    --ink: #1f1f1f;
    --paper: #ffffff;
    --sky: #8fdbe3;
    --tree: #4f7a2a;
    --grass: #68b52a;
    --grass-light: #93cf3a;
    --badge: #d9d9d9;
    --brand: #8dbb3a;
  }
  html, body {
    margin: 0;
    width: 1200px;
    height: 880px;
    overflow: hidden;
    background: var(--page);
  }
  .sheet {
    position: relative;
    width: 1200px;
    height: 880px;
    font-family: "Carlito", "Calibri", sans-serif;
  }
  .banner { position: absolute; display: block; }
  .banner--portrait { left: 48px; top: 35px; width: 360px; height: 792px; }
  .banner--scene { left: 466px; top: 32px; width: 430px; height: 254px; }
  .banner--landscape { left: 464px; top: 361px; width: 634px; height: 465px; }
  .neu { font-weight: 700; fill: var(--sun); }
  .claim, .slogan, .contact { fill: var(--ink); font-weight: 400; }
  .brand-name { fill: var(--brand); font-weight: 700; }
  .yellow-band { fill: var(--sun); }
  .green-panel { fill: var(--leaf); }
  .white-field { fill: var(--paper); }
  .badge-shape { fill: var(--badge); }
</style>
</head>
<body>
<main class="sheet">
  <svg class="banner banner--portrait" viewBox="0 0 360 792" font-family="Carlito, Calibri, sans-serif">
    <defs>
      <linearGradient id="meadowTall" x1="0" y1="0" x2="0" y2="1">
        <stop offset="0" stop-color="var(--sky)"/>
        <stop offset="0.2" stop-color="var(--tree)"/>
        <stop offset="0.36" stop-color="var(--grass-light)"/>
        <stop offset="1" stop-color="var(--grass)"/>
      </linearGradient>
      <linearGradient id="printTall" x1="0" y1="0" x2="1" y2="1">
        <stop offset="0" stop-color="#7aa04a"/>
        <stop offset="0.5" stop-color="#b0703a"/>
        <stop offset="1" stop-color="#c9d8a8"/>
      </linearGradient>
    </defs>
    <rect class="scene-photo" width="360" height="792" fill="url(#meadowTall)" role="img" aria-label="Weißes Wohnmobil mit ausgefahrener Markise auf einer grünen Wiese vor Bäumen"/>
    <rect class="awning-print" x="36" y="140" width="197" height="140" fill="url(#printTall)" role="img" aria-label="Bedruckter Sunblocker mit einem braunen Welpen im Blumenfeld"/>
    <path class="yellow-band" d="M0,792 C0,500 150,304 360,304 L360,792 Z"/>
    <path class="green-panel" d="M12,792 C14,520 165,322 360,322 L360,792 Z"/>
    <path class="white-field" d="M360,396 C250,440 220,640 312,792 L360,792 Z"/>
    <text class="neu" x="135" y="481" font-size="56">NEU</text>
    <text class="claim" font-size="21">
      <tspan x="81" y="511">INDIVIDUELL</tspan>
      <tspan x="81" y="538">BEDRUCKBARE</tspan>
      <tspan x="81" y="565">SUNBLOCKER</tspan>
    </text>
    <text class="slogan" font-size="23">
      <tspan x="39" y="633">Für den schönsten</tspan>
      <tspan x="39" y="661">Schatten der Welt!</tspan>
    </text>
    <text class="contact" font-size="14">
      <tspan x="40" y="707">Kontakt Information:</tspan>
      <tspan x="40" y="725">bild@graylindtrailgear.com</tspan>
    </text>
    <rect class="badge-shape" x="254" y="532" width="56" height="46" rx="6"/>
    <text class="brand-name" font-size="16">
      <tspan x="255" y="612">Graylind</tspan>
      <tspan x="255" y="630">Trail Gear</tspan>
    </text>
  </svg>

  <svg class="banner banner--scene" viewBox="0 0 430 254" font-family="Carlito, Calibri, sans-serif">
    <defs>
      <linearGradient id="meadowWide" x1="0" y1="0" x2="0" y2="1">
        <stop offset="0" stop-color="var(--sky)"/>
        <stop offset="0.25" stop-color="var(--tree)"/>
        <stop offset="0.5" stop-color="var(--grass-light)"/>
        <stop offset="1" stop-color="var(--grass)"/>
      </linearGradient>
      <linearGradient id="printSmall" x1="0" y1="0" x2="1" y2="1">
        <stop offset="0" stop-color="#7aa04a"/>
        <stop offset="0.5" stop-color="#b0703a"/>
        <stop offset="1" stop-color="#c9d8a8"/>
      </linearGradient>
    </defs>
    <rect class="scene-photo" width="430" height="254" fill="url(#meadowWide)" role="img" aria-label="Weißes Wohnmobil mit großer Markise auf einer Wiese"/>
    <rect x="43" y="62" width="237" height="174" fill="#e9efe4"/>
    <rect class="awning-print" x="76" y="79" width="120" height="81" fill="url(#printSmall)" role="img" aria-label="Wohnmobil mit Welpenmotiv auf der Markise"/>
    <path class="yellow-band" d="M43,236 C90,180 180,154 280,154 L280,236 Z"/>
    <path class="green-panel" d="M50,236 C97,187 185,162 280,162 L280,236 Z"/>
    <path class="white-field" d="M280,172 C230,180 210,210 218,236 L280,236 Z"/>
    <text class="neu" x="112" y="206" font-size="20">NEU</text>
    <text class="claim" font-size="7">
      <tspan x="160" y="184">INDIVIDUELL</tspan>
      <tspan x="160" y="193.5">BEDRUCKBARE</tspan>
      <tspan x="160" y="203">SUNBLOCKER</tspan>
    </text>
    <text class="slogan" x="76" y="214" font-size="7.8">Für den schönsten Schatten der Welt!</text>
    <text class="contact" x="76" y="223" font-size="4.8">Kontakt Information: bild@graylindtrailgear.com</text>
    <rect class="badge-shape" x="235" y="188" width="30" height="14" rx="2"/>
    <text class="brand-name" x="229" y="215" font-size="6">Graylind Trail Gear</text>
  </svg>

  <svg class="banner banner--landscape" viewBox="0 0 634 465" font-family="Carlito, Calibri, sans-serif">
    <defs>
      <linearGradient id="meadowLarge" x1="0" y1="0" x2="0" y2="1">
        <stop offset="0" stop-color="var(--sky)"/>
        <stop offset="0.18" stop-color="var(--tree)"/>
        <stop offset="0.42" stop-color="var(--grass-light)"/>
        <stop offset="1" stop-color="var(--grass)"/>
      </linearGradient>
      <linearGradient id="printLarge" x1="0" y1="0" x2="1" y2="1">
        <stop offset="0" stop-color="#7aa04a"/>
        <stop offset="0.5" stop-color="#b0703a"/>
        <stop offset="1" stop-color="#c9d8a8"/>
      </linearGradient>
    </defs>
    <rect class="scene-photo" width="634" height="465" fill="url(#meadowLarge)" role="img" aria-label="Weißes Wohnmobil mit ausgefahrener Markise auf einer grünen Wiese vor Bäumen"/>
    <rect class="awning-print" x="94" y="46" width="315" height="211" fill="url(#printLarge)" role="img" aria-label="Bedruckter Sunblocker mit einem braunen Welpen im Blumenfeld"/>
    <path class="yellow-band" d="M0,465 C150,300 400,242 634,242 L634,465 Z"/>
    <path class="green-panel" d="M14,465 C170,318 410,260 634,260 L634,465 Z"/>
    <path class="white-field" d="M634,290 C520,300 460,380 475,465 L634,465 Z"/>
    <text class="neu" x="187" y="383" font-size="50">NEU</text>
    <text class="claim" font-size="20">
      <tspan x="314" y="332">INDIVIDUELL</tspan>
      <tspan x="314" y="357">BEDRUCKBARE</tspan>
      <tspan x="314" y="382">SUNBLOCKER</tspan>
    </text>
    <text class="slogan" x="88" y="412" font-size="21.5">Für den schönsten Schatten der Welt!</text>
    <text class="contact" x="88" y="433" font-size="13">Kontakt Information: bild@graylindtrailgear.com</text>
    <rect class="badge-shape" x="507" y="332" width="56" height="46" rx="6"/>
    <text class="brand-name" font-size="16">
      <tspan x="500" y="404">Graylind</tspan>
      <tspan x="500" y="422">Trail Gear</tspan>
    </text>
  </svg>
</main>
</body>
</html>
```